Micro-Marketing and Vending Brochure

I am looking for an elegant, fun, eye catching brochure that will highlight my new business to protential clients in the Hotel, College/University and Hospital industry. please find pictures of Micro-Markets on line and on my website, to make a fun, professional and elegant design, use color scheme from website, and logo and a few picture will be attach to this email. This is a new business and i would like to represent my company in the best possible way, please take time with this project, color, front and wording is very important along with pics. I have a image of a micro-Market please take out the BRISKO and place file logo of TORN..please let me know if more information is needed for this project to be successful

```html
<!DOCTYPE html>
<html lang="en">
<head>
<meta charset="utf-8">
<title>RVL Markets – Healthy, Happy Snack People</title>
<link rel="stylesheet" href="https://fonts.googleapis.com/css2?family=Raleway:wght@400;500;700;800&display=swap">
<style>
  :root {
    --yellow: #f8c940;
    --yellow-soft: #fde9a6;
    --yellow-pale: #fff4d0;
    --panel: #f3dc9a;
    --ink: #3a3a3a;
    --text: #444444;
    --bullet: #9d95aa;
    --sky: #cfe6f5;
    --band: #cde4f4;
    --grass: #a9cf72;
    --white: #ffffff;
  }
  * { box-sizing: border-box; margin: 0; padding: 0; }
  html, body { width: 848px; height: 1200px; overflow: hidden; background: var(--white); }
  body { font-family: "Raleway", sans-serif; color: var(--text); }
  .brochure { position: relative; width: 848px; height: 1200px; overflow: hidden; background: var(--white); }

  .backdrop {
    position: absolute; left: 0; top: 560px; width: 848px; height: 640px;
    background: linear-gradient(180deg, #ffffff 0%, #e3f0f9 20%, var(--sky) 45%, #e4efe0 72%, var(--grass) 100%);
  }

  .photo-panel { position: absolute; left: 412px; top: 0; width: 436px; height: 540px; background: var(--panel); }
  .photo { position: absolute; }
  .photo--coffee { left: 424px; top: 26px; width: 233px; height: 198px; background: linear-gradient(135deg, #3b3d44, #8a8e96 60%, #2b2c30); }
  .photo--juice { left: 671px; top: 26px; width: 159px; height: 198px; background: linear-gradient(160deg, #fff4e0, #f6a623 55%, #e98a12); }
  .photo--snacks { left: 424px; top: 236px; width: 233px; height: 152px; background: linear-gradient(180deg, #5a3d2a, #b8875a 50%, #6b4a31); }
  .photo--salad { left: 671px; top: 236px; width: 159px; height: 152px; background: linear-gradient(135deg, #e9ddc8, #7aa23b 50%, #c23a3a); }
  .photo--bars { left: 424px; top: 400px; width: 405px; height: 128px; background: linear-gradient(90deg, #3a2418, #7b4a2c 35%, #c7a27a 55%, #6b3a22 80%, #2a1a12); }
  .photo--products { left: 572px; top: 775px; width: 166px; height: 240px; background: linear-gradient(180deg, #6c4a2e 0%, #c99c5a 35%, #7cae42 65%, #e7a028 100%); border-radius: 6px; }

  .ribbon {
    position: absolute; left: 0; height: 48px;
    background: linear-gradient(180deg, var(--yellow-soft), var(--yellow));
    border-bottom: 3px solid #e5c35e;
    display: flex; align-items: center; padding-left: 32px;
  }
  .ribbon h2 { font-size: 24px; font-weight: 700; color: var(--ink); letter-spacing: 0.1px; }
  .ribbon svg { position: absolute; right: 0; top: 0; }
  .ribbon--top { top: 0; width: 397px; height: 72px; padding-left: 6px; padding-top: 14px; background: linear-gradient(180deg, var(--yellow-pale), var(--yellow)); left: 26px; }
  .ribbon--easy { top: 319px; width: 397px; }
  .ribbon--cool { top: 466px; width: 397px; }
  .ribbon--kiosk { top: 807px; width: 415px; padding-left: 28px; }

  .audience { position: absolute; left: 38px; top: 85px; font-size: 14.5px; line-height: 19px; }
  .audience li { list-style: none; }
  .audience li.sub { padding-left: 32px; }

  .bullets { list-style: none; font-size: 15px; line-height: 20px; }
  .bullets li { position: relative; padding-left: 32px; }
  .bullets li::before { content: ""; position: absolute; left: 1px; top: 5px; width: 10px; height: 10px; background: var(--bullet); }
  .benefits { position: absolute; left: 38px; top: 160px; }
  .facts { position: absolute; left: 30px; top: 559px; width: 720px; font-size: 14.5px; line-height: 17px; }
  .facts li { margin-bottom: 2px; }
  .kiosk-list { position: absolute; left: 30px; top: 879px; width: 400px; line-height: 19px; }
  .kiosk-list li { margin-bottom: 3px; }

  .copy { position: absolute; left: 38px; width: 360px; font-size: 14.5px; line-height: 18.5px; text-align: justify; }
  .copy--intro { top: 235px; }
  .copy--tech { top: 394px; }

  .fact-tag { position: absolute; left: 32px; top: 521px; width: 77px; height: 25px; background: var(--yellow); color: var(--white); font-size: 21px; font-weight: 800; line-height: 25px; padding-left: 5px; }

  .band { position: absolute; left: 0; top: 646px; width: 848px; height: 88px; background: var(--band); display: flex; align-items: center; justify-content: center; }
  .band h1 { font-size: 30px; font-weight: 800; color: var(--ink); text-align: center; line-height: 36px; letter-spacing: 0.3px; }
  .tagline { position: absolute; left: 40px; top: 746px; width: 768px; text-align: center; font-size: 15px; line-height: 19px; color: var(--ink); }

  .brand { position: absolute; left: 580px; top: 1058px; display: flex; align-items: center; gap: 12px; }
  .brand-mark { width: 40px; height: 40px; background: var(--bullet); }
  .brand-name { font-size: 52px; font-weight: 800; color: var(--yellow); letter-spacing: 4px; line-height: 52px; }

  .contact { position: absolute; left: 590px; top: 1126px; font-size: 13px; line-height: 17px; color: var(--ink); list-style: none; }
  .contact li { display: flex; align-items: center; gap: 14px; }
</style>
</head>
<body>
<main class="brochure">
  <div class="backdrop" role="img" aria-label="Soft sky and green meadow background"></div>

  <div class="photo-panel"></div>
  <div class="photo photo--coffee" role="img" aria-label="Coffee brewing station with pod rack"></div>
  <div class="photo photo--juice" role="img" aria-label="Bottles of orange juice"></div>
  <div class="photo photo--snacks" role="img" aria-label="Micro-market snack shelves"></div>
  <div class="photo photo--salad" role="img" aria-label="Fresh chicken salad with berries"></div>
  <div class="photo photo--bars" role="img" aria-label="Row of chocolate bars in a vending machine"></div>

  <header class="ribbon ribbon--top"><h2>Healthy, Happy Snack People</h2></header>

  <ul class="audience">
    <li>For&nbsp; a) Hotels</li>
    <li class="sub">b) Colleges and Universities</li>
    <li class="sub">c) Hospitals</li>
  </ul>

  <ul class="bullets benefits">
    <li>Boost Employee/Clients/ patients&nbsp; Morale</li>
    <li>Increase Productivity</li>
    <li>Support employee Healthy lifestyle</li>
  </ul>

  <p class="copy copy--intro">RVL Markets LLC Micro-Markets and Vending system allows you to select form hundreds of healthy, tasty and nutritional balance options.&nbsp; We have healthy snack and fresh produce</p>

  <section class="ribbon ribbon--easy">
    <h2>Easy Convenient Healthy</h2>
    <svg width="34" height="48" viewBox="0 0 34 48"><polygon points="0,0 34,0 34,34" fill="#e9b21f"/></svg>
  </section>

  <p class="copy copy--tech">Our Micro Markets are state of Art, with advance technology, credit card, debit card, self-check out Kiosk system, tracks calories and each item before purchase</p>

  <section class="ribbon ribbon--cool">
    <h2>HOW COOL IS THAT!!!</h2>
    <svg width="34" height="48" viewBox="0 0 34 48"><polygon points="0,0 34,0 34,34" fill="#e9b21f"/></svg>
  </section>

  <div class="fact-tag">FACT:</div>

  <ul class="bullets facts">
    <li>One-third of U.S Adults (33.8%) are considered<br>obese</li>
    <li>Poor Diet can lead to decreased performance and productivity at the office, school &amp; Home</li>
    <li>Unhealthy workers cost employers and average of 12,000 per year per employee</li>
  </ul>

  <section class="band">
    <h1>LETS MAKE A CHANGE AND BECOME HEALTHY,<br>HAPPY SNACK PEOPLE</h1>
  </section>

  <p class="tagline">Smart snacking is proving not to be a short-lived health fad, but rather a top priority among a growing number of consumers.</p>

  <section class="ribbon ribbon--kiosk">
    <h2>KIOSK and VENDING SYSTEM</h2>
    <svg width="34" height="48" viewBox="0 0 34 48"><polygon points="0,0 34,0 34,34" fill="#e9b21f"/></svg>
  </section>

  <ul class="bullets kiosk-list">
    <li>Remote wireless and Sales monitoring</li>
    <li>Security Monitoring</li>
    <li>Accepts Credit Card and debet card, cash and coins, bid coins,</li>
    <li>Electronic payment types, Glide Wallet Brisko Pay, PayNest (etc) ...</li>
    <li>Employee user accounts</li>
    <li>Accomadates chilled , non-chilled, fresh produce and micro-Waveables.</li>
  </ul>

  <div class="photo photo--products" role="img" aria-label="Healthy snack packages: energy bar, pita chips, fruit pouch and fruit snacks"></div>

  <div class="brand">
    <span class="brand-mark"></span>
    <span class="brand-name">RVL</span>
  </div>

  <ul class="contact">
    <li>
      <svg width="10" height="15" viewBox="0 0 10 15"><rect x="1" y="0.5" width="8" height="14" rx="1.5" fill="none" stroke="#3a3a3a" stroke-width="1.2"/><rect x="3.5" y="12" width="3" height="1" fill="#3a3a3a"/></svg>
      <span>(800) 555–0148</span>
    </li>
    <li>
      <svg width="12" height="12" viewBox="0 0 12 12"><circle cx="6" cy="6" r="5.2" fill="none" stroke="#3a3a3a" stroke-width="1.1"/><line x1="1" y1="6" x2="11" y2="6" stroke="#3a3a3a" stroke-width="1"/><ellipse cx="6" cy="6" rx="2.3" ry="5.2" fill="none" stroke="#3a3a3a" stroke-width="1"/></svg>
      <span>www.rvlmarkets.com</span>
    </li>
  </ul>
</main>
</body>
</html>
```